Clinician Supply Circle

I am a financial planner whose client's are physicians and dentists. As physicians, there is very little time for them to do research on numerous aspects of their business and personal lives. I am looking to build a website that is a 1 stop shop for many of the services/resources they may need. It will be my job to screen the resources/advertisers and place competent people/business's that I know and have a track record on. there will ultimately be 10 or 12 ish areas that I would like to provide resources in:
disability insurance
life insurance
retirement planning
student loan advisors
employment contract and business formation attorneys
accountants
real estate agents
physician mortgages
personal loans
malpractice insurance
physician recruiters
maybe 2 other areas which I have yet to figure out.....
I would like each of these options to be able to be clicked on and a page will open up with the 1 or 2 or 3 or 4 people/business's that I have picked to represent these areas. I would like each specific person/business to have a click here to contact me link in which an email goes to the person and I am copied on the initial correspondence between the physician and the mortgage broker.... just so I can see some of the correspondence they will be receiving.
nowhere on the site do I want it to say my name. there will be certain disclosures that are needed and other wording but I think this is a good starting point.
here are links to two websites with the same general concept. please keep in mind that I want my website to be more on the simple side.
http://www.quillbarrowpartners.example/index.html
http://fernlakeledger.example/
Updates
Industry/Entity Type
Financial

```html
<!DOCTYPE html>
<html lang="en">
<head>
<meta charset="utf-8">
<title>Clinician Supply Circle</title>
<link href="https://fonts.googleapis.com/css2?family=Open+Sans:wght@300;400;600;700&family=Oswald:wght@500;700&display=swap" rel="stylesheet">
<style>
:root{
  --blue:#1d6fc7;
  --blue-dark:#14549e;
  --ink:#222;
  --text:#555;
  --muted:#999;
  --white:#fff;
  --hero-a:#3d5f86;
  --hero-b:#9fb4cc;
  --footer-a:#3b3b3b;
  --footer-b:#1f1f1f;
  --copy-bg:#111;
  --orange:#e07b14;
  --ad-red:#d01b1b;
}
*{box-sizing:border-box;margin:0;padding:0}
html,body{width:1200px;height:3126px;overflow:hidden;background:var(--white)}
body{position:relative;font-family:"Open Sans",Arial,sans-serif;color:var(--text)}
.abs{position:absolute}
a{text-decoration:none;color:inherit}

/* header */
.brand{left:86px;top:70px;font-size:37px;font-weight:600;color:var(--ink);letter-spacing:-.3px}
.brand span{color:var(--blue)}
.nav a{position:absolute;top:77px;height:36px;line-height:36px;font-size:16px;color:var(--ink);text-transform:uppercase}
.nav .active{background:var(--blue);color:var(--white);padding:0 15px;left:722px}

/* hero */
.hero{left:0;top:167px;width:1200px;height:539px;background:linear-gradient(120deg,var(--hero-b),var(--hero-a) 55%,#1e3350)}
.hero-caption{left:338px;top:478px;width:533px;height:136px;background:rgba(36,104,190,.78);color:var(--white);font-size:28px;line-height:46px;padding:22px 34px;text-transform:uppercase}
.dots{left:580px;top:662px;display:flex;gap:6px}
.dots i{width:16px;height:16px;border-radius:50%;background:rgba(255,255,255,.75)}
.dots i:first-child{background:var(--white)}

/* services */
.section-title{left:0;width:1200px;top:764px;text-align:center;font-size:37px;font-weight:300;color:var(--ink)}
.section-title b{font-weight:400;color:var(--blue)}
.intro{left:97px;width:1008px;top:844px;text-align:center;font-size:13.5px;line-height:24px}
.service{width:360px;text-align:center}
.service .icon{display:block;margin:0 auto}
.service h3{font-size:21px;font-weight:400;color:var(--blue);margin-top:20px}
.service hr{width:70px;border:0;border-top:1px solid #ddd;margin:12px auto 14px}
.service p{font-size:13.5px;line-height:23px}
.service a{display:block;color:var(--blue);font-size:13.5px;font-weight:600;margin-top:11px}

/* welcome */
.welcome h2{font-size:30px;font-weight:400;color:var(--ink)}
.welcome p{margin-top:18px;font-size:13.5px;line-height:22.5px;width:600px}
.btn-more{left:88px;top:2082px;width:140px;height:36px;border:2px solid var(--blue);border-radius:18px;color:var(--blue);font-size:14px;font-weight:600;display:flex;align-items:center;justify-content:center;gap:14px}
.promo{left:767px;top:1854px;width:345px;height:273px;background:linear-gradient(90deg,#c9d3dc,#8fa6ba)}
.promo-text{left:917px;top:1905px;width:185px;color:var(--white)}
.promo-text h4{font-size:21px;font-weight:400;line-height:29px}
.promo-text .sub{font-size:12.5px;color:#cfe6ff;margin-top:10px;line-height:17px}
.promo-text .tel{font-size:14px;margin-top:12px}
.promo-text .quote{display:inline-block;margin-top:12px;background:var(--orange);font-size:13px;padding:3px 10px}

/* blog */
.blog-title{left:86px;top:2206px;font-size:30px;color:var(--ink)}
.post{left:88px;width:600px;display:flex;gap:16px}
.post .thumb{width:65px;height:60px;flex:none;background:linear-gradient(135deg,#c6d4e0,#7b8fa6)}
.post h5{font-size:16px;font-weight:400;color:var(--blue)}
.post p{font-size:13.5px;line-height:22px;margin-top:6px}
.post small{color:var(--muted);font-size:12.5px}

/* ad */
.ad{left:767px;top:2211px;width:345px;height:327px;border:5px solid var(--ad-red);background:var(--white);text-align:center;font-family:"Oswald",Arial,sans-serif}
.ad .bank{font-size:13px;color:var(--ink);margin-top:6px;letter-spacing:1px}
.ad .head{font-size:25px;font-weight:700;color:var(--ad-red);line-height:28px}
.ad .head2{font-size:25px;font-weight:700;color:var(--ink);line-height:28px}
.ad .pmi{font-size:16px;font-style:normal;color:var(--ink)}
.ad .portrait{position:absolute;left:8px;top:112px;width:150px;height:170px;background:linear-gradient(180deg,#b58a6a,#6b4a3a)}
.ad .info{position:absolute;left:165px;top:116px;width:165px;text-align:center;font-size:13px;color:var(--ink);line-height:18px}
.ad .info b{display:block;font-size:17px;color:var(--ad-red)}
.ad .lender{margin-top:10px;font-size:17px;font-weight:700;color:var(--ad-red)}
.ad .foot{position:absolute;left:0;bottom:0;width:100%;height:30px;background:var(--ad-red);color:var(--white);font-size:15px;line-height:30px;letter-spacing:1px}

/* newsletter */
.newsletter{left:0;top:2570px;width:1200px;height:196px;background:linear-gradient(100deg,#1460b8,#2b86d8 70%,#1f73c7)}
.newsletter h2{position:absolute;left:86px;top:105px;font-size:35px;font-weight:600;color:var(--white)}
.newsletter .field{position:absolute;left:747px;top:112px;width:239px;height:46px;border:1px solid rgba(255,255,255,.6);color:var(--white);font-size:14px;line-height:44px;padding-left:18px}
.newsletter .submit{position:absolute;left:986px;top:112px;width:126px;height:46px;background:var(--blue-dark);color:var(--white);font-size:16px;line-height:46px;text-align:center}

/* footer */
.footer{left:0;top:2766px;width:1200px;height:289px;background:linear-gradient(180deg,var(--footer-a),var(--footer-b))}
.fcol{top:2804px;color:var(--white)}
.fcol h6{font-size:18px;font-weight:400;margin-bottom:14px}
.fcol li{list-style:none;font-size:14px;line-height:32.5px;color:#e8e8e8}
.contact-line{display:flex;gap:10px;font-size:14px;color:#e8e8e8;line-height:26px}
.social{left:871px;top:2970px;display:flex;gap:9px}
.social i{width:28px;height:28px;border-radius:50%;background:#777}
.copy{left:0;top:3055px;width:1200px;height:71px;background:var(--copy-bg);color:var(--white);font-size:13px;padding:22px 0 0 92px}
</style>
</head>
<body>

<header>
  <div class="abs brand"><span>CLINICIAN</span> SUPPLY CIRCLE</div>
  <nav class="nav">
    <a class="active" href="#">Home</a>
    <a href="#" style="left:821px">About Us</a>
    <a href="#" style="left:936px">Services</a>
    <a href="#" style="left:1044px">Contact</a>
  </nav>
</header>

<section class="abs hero" role="img" aria-label="Photo of two professionals reviewing documents at a desk"></section>
<div class="abs hero-caption">Maecenas sed diam eget risvari us blandit sit amet non</div>
<div class="abs dots"><i></i><i></i><i></i></div>

<h2 class="abs section-title">OUR <b>SERVICES</b></h2>
<p class="abs intro">Claritas est etiam processus dynamicus, qui sequitur mutationem consuetudium lectorum. Mirum est notare quam littera gothica, quam nunc putamus parum claram ut aliquip ex ea commodo consequat. Duis autem vel eum iriure dolor in hendrerit in vulputate velit esse molestie consequat, vel illum</p>

<!-- service grid -->
<div class="abs service" style="left:41px;top:940px">
  <svg class="icon" width="70" height="70" viewBox="0 0 70 70"><rect x="13" y="13" width="44" height="44" transform="rotate(45 35 35)" fill="var(--blue)"/><circle cx="35" cy="35" r="9" fill="none" stroke="#fff" stroke-width="3"/><circle cx="35" cy="35" r="3" fill="#fff"/></svg>
  <h3>Disability Insurance</h3><hr>
  <p>Claritas est eteus dynamicuinqui sequtatiem<br>conetlaritasdynamicusClaritas est.</p>
  <a href="#">Click here to contact me &gt;&gt;</a>
</div>
<div class="abs service" style="left:420px;top:940px">
  <svg class="icon" width="70" height="70" viewBox="0 0 70 70"><rect x="13" y="13" width="44" height="44" transform="rotate(45 35 35)" fill="var(--blue)"/><path d="M24 40h8l6 4h8v-4h-6M30 28a5 5 0 1 1 10 0c0 4-5 6-5 8" fill="none" stroke="#fff" stroke-width="3"/></svg>
  <h3>Life Insurance</h3><hr>
  <p>Claritas est eteus dynamicuinqui sequtatiem<br>conetlaritasdynamicusClaritas est.</p>
  <a href="#">Click here to contact me &gt;&gt;</a>
</div>
<div class="abs service" style="left:797px;top:940px">
  <svg class="icon" width="70" height="70" viewBox="0 0 70 70"><rect x="13" y="13" width="44" height="44" transform="rotate(45 35 35)" fill="var(--blue)"/><rect x="27" y="24" width="16" height="22" fill="none" stroke="#fff" stroke-width="2.5"/><path d="M31 31h8M31 35h8M31 39h8" stroke="#fff" stroke-width="2"/></svg>
  <h3>Retirement Planning</h3><hr>
  <p>Claritas est eteus dynamicuinqui sequtatiem<br>conetlaritasdynamicusClaritas est.</p>
  <a href="#">Click here to contact me &gt;&gt;</a>
</div>

<div class="abs service" style="left:41px;top:1228px">
  <svg class="icon" width="70" height="70" viewBox="0 0 70 70"><rect x="13" y="13" width="44" height="44" transform="rotate(45 35 35)" fill="var(--blue)"/><path d="M21 32l14-7 14 7-14 7z" fill="#fff"/><path d="M27 36v6c4 3 12 3 16 0v-6" fill="#fff"/></svg>
  <h3>Student Loan Advisors</h3><hr>
  <p>Claritas est eteus dynamicuinqui sequtatiem<br>conetlaritasdynamicusClaritas est.</p>
  <a href="#">Click here to contact me &gt;&gt;</a>
</div>
<div class="abs service" style="left:420px;top:1228px">
  <svg class="icon" width="70" height="70" viewBox="0 0 70 70"><rect x="13" y="13" width="44" height="44" transform="rotate(45 35 35)" fill="var(--blue)"/><rect x="26" y="24" width="16" height="22" fill="none" stroke="#fff" stroke-width="2.5"/><path d="M36 42l10-12" stroke="#fff" stroke-width="3"/></svg>
  <h3>Employment Contract</h3><hr>
  <p>Claritas est eteus dynamicuinqui sequtatiem<br>conetlaritasdynamicusClaritas est.</p>
  <a href="#">Click here to contact me &gt;&gt;</a>
</div>
<div class="abs service" style="left:797px;top:1228px">
  <svg class="icon" width="70" height="70" viewBox="0 0 70 70"><rect x="13" y="13" width="44" height="44" transform="rotate(45 35 35)" fill="var(--blue)"/><circle cx="35" cy="30" r="6" fill="#fff"/><path d="M24 46c2-7 20-7 22 0z" fill="#fff"/></svg>
  <h3>Accountants</h3><hr>
  <p>Claritas est eteus dynamicuinqui sequtatiem<br>conetlaritasdynamicusClaritas est.</p>
  <a href="#">Click here to contact me &gt;&gt;</a>
</div>

<div class="abs service" style="left:41px;top:1517px">
  <svg class="icon" width="70" height="70" viewBox="0 0 70 70"><rect x="13" y="13" width="44" height="44" transform="rotate(45 35 35)" fill="var(--blue)"/><path d="M23 34l12-9 12 9v11H23z" fill="#fff"/><rect x="32" y="38" width="6" height="7" fill="var(--blue)"/></svg>
  <h3>Real Estate Agents</h3><hr>
  <p>Claritas est eteus dynamicuinqui sequtatiem<br>conetlaritasdynamicusClaritas est.</p>
  <a href="#">Click here to contact me &gt;&gt;</a>
</div>
<div class="abs service" style="left:420px;top:1517px">
  <svg class="icon" width="70" height="70" viewBox="0 0 70 70"><rect x="13" y="13" width="44" height="44" transform="rotate(45 35 35)" fill="var(--blue)"/><path d="M25 45l20-20M25 25l20 20" stroke="#fff" stroke-width="3.5" stroke-linecap="round"/></svg>
  <h3>Physician Mortgages</h3><hr>
  <p>Claritas est eteus dynamicuinqui sequtatiem<br>conetlaritasdynamicusClaritas est.</p>
  <a href="#">Click here to contact me &gt;&gt;</a>
</div>
<div class="abs service" style="left:797px;top:1517px">
  <svg class="icon" width="70" height="70" viewBox="0 0 70 70"><rect x="13" y="13" width="44" height="44" transform="rotate(45 35 35)" fill="var(--blue)"/><rect x="24" y="27" width="22" height="16" fill="none" stroke="#fff" stroke-width="2.5"/><circle cx="31" cy="34" r="2.5" fill="#fff"/><path d="M36 33h7M36 37h7" stroke="#fff" stroke-width="2"/></svg>
  <h3>Personal Loans</h3><hr>
  <p>Claritas est eteus dynamicuinqui sequtatiem<br>conetlaritasdynamicusClaritas est.</p>
  <a href="#">Click here to contact me &gt;&gt;</a>
</div>

<!-- welcome -->
<section class="abs welcome" style="left:88px;top:1858px">
  <h2>Welcome to our website</h2>
  <p>Claritas est etiam processus dynamicus, qui sequitur mutationem consuetudium lectorum. Mirum est notare quam littera gothica, quam nunc putamus parum claram, anteposuerit litterarum formas humanitatis per digmissim qui blandit facer possim assum.<br>Duis autem vel eum iriure dolor in hendrerit in vulputate velit esse molestie consequat, vel illum dolore eu feugiat nulla facilisis at vero eros et accumsanet iusto odio dignissim qui blandit praesent luptatum zzril delenit facer possim assum.</p>
</section>
<a class="abs btn-more" href="#">Read More
  <svg width="16" height="12" viewBox="0 0 16 12"><path d="M1 6h13M9 1l5 5-5 5" fill="none" stroke="currentColor" stroke-width="2"/></svg></a>

<div class="abs promo" role="img" aria-label="Photo of a hand holding a stethoscope"></div>
<div class="abs promo-text">
  <h4>Disablity Insurance for Physicians</h4>
  <div class="sub">Empowering physicians<br>to protect their income</div>
  <div class="tel">+00 555 010 927</div>
  <span class="quote">Get Quote</span>
</div>

<!-- blog -->
<h2 class="abs blog-title">Recent Blog Posts</h2>
<article class="abs post" style="top:2274px">
  <div class="thumb" role="img" aria-label="Thumbnail photo of a desk with papers"></div>
  <div><h5>Ut wisi enim ad minim veniam quis nostrud</h5>
  <p>Mirum est notare quam littera gothica, quam nunc putamus parum claram, antepo suerit litterarum mirum est notare quam littera gothica. <small>1 hour ago</small></p></div>
</article>
<article class="abs post" style="top:2372px">
  <div class="thumb" role="img" aria-label="Thumbnail photo of a doctor"></div>
  <div><h5>Claritas est etiam processus dynamicus</h5>
  <p>Mirum est notare quam littera gothica, quam nunc putamus parum claram, antepo suerit litterarum mirum est notare quam littera gothica. <small>1 hour ago</small></p></div>
</article>
<article class="abs post" style="top:2471px">
  <div class="thumb" role="img" aria-label="Thumbnail photo of a medical professional"></div>
  <div><h5>Eodem modo typi, qui nunc nobis videntur parum clari</h5>
  <p>Mirum est notare quam littera gothica, quam nunc putamus parum claram, antepo suerit litterarum mirum est notare quam littera gothica. <small>1 hour ago</small></p></div>
</article>

<!-- advertiser -->
<aside class="abs ad">
  <div class="bank">THE HARBOR MILL BANK</div>
  <div class="head">DOCTOR AND DENTIST</div>
  <div class="head2">100% LOAN PROGRAM</div>
  <div class="pmi">NO PMI</div>
  <div class="portrait" role="img" aria-label="Portrait photo of the mortgage loan officer"></div>
  <div class="info">
    <b>MARION KELLER</b>MORTGAGE LOAN OFFICER<br><br>555.014.2290<br>NMLSR# 000000<br>AL, FL, GA, SC, TN
    <div class="lender">TOLLGATE LENDING</div>
  </div>
  <div class="foot">22 YEARS OF EXPERIENCE</div>
</aside>

<!-- newsletter -->
<section class="abs newsletter">
  <h2>Subscribe to our Newsletter</h2>
  <div class="field">E-mail Address</div>
  <div class="submit">SUBSCRIBE</div>
</section>

<!-- footer -->
<footer class="abs footer"></footer>
<div class="abs fcol" style="left:95px"><h6>LINKS</h6><ul><li>Privacy Policy</li><li>About Us</li><li>Track Order</li><li>Store Locator</li><li>Brand Houses</li><li>Gift Cards</li></ul></div>
<div class="abs fcol" style="left:325px"><h6>LINKS</h6><ul><li>Typi non haben</li><li>Successful Campaigns</li><li>New Campaigns</li><li>Ending Soon</li><li>Most Funded Campaigns</li><li>lorem ipsum</li></ul></div>
<div class="abs fcol" style="left:611px"><h6>LINKS</h6><ul><li>Typi non haben</li><li>Successful Campaigns</li><li>New Campaigns</li><li>Ending Soon</li><li>Most Funded Campaigns</li><li>lorem ipsum</li></ul></div>
<div class="abs fcol" style="left:871px"><h6>CONTACT</h6>
  <div class="contact-line"><svg width="14" height="26" viewBox="0 0 14 26"><path d="M3 8c0 6 4 11 9 12l1-3-3-2-2 2c-2-1-3-3-4-5l2-2-2-3z" fill="#aaa"/></svg><span style="padding-left:8px">555 010 448</span></div>
  <div class="contact-line" style="margin-top:12px"><svg width="14" height="26" viewBox="0 0 14 26"><path d="M7 3a5 5 0 0 1 5 5c0 4-5 9-5 9S2 12 2 8a5 5 0 0 1 5-5z" fill="#aaa"/></svg><span style="padding-left:8px">4820 Alder Crest Rd. #210<br>Willow Bend, CA 90000</span></div>
</div>
<div class="abs social"><i></i><i></i><i></i><i></i></div>
<div class="abs copy">Copyright ©2013. All Rights Reserved.</div>

</body>
</html>
```